Vorelin
Montclaro SAS
Vorelin - Personal Care
Modern
Lucila Barrios Quintero
Presidente
Av. Carrera 57 #18B-64 Bogota, Colombia
lucilabarriosquintero@correoplum.net
www.vorelin-demo.net
Vorelin is the brand;s name Montclaro SAS is the firm´s name We sell shampoo and hair tonic. çthey are good quality products, for elegant consumers.
One side can go Vorelin, the other side Montclaro, for instance. Vorelin is the important one, Vorelin has a logo I want the principal side of the business card with white background and blue letters. The other side blue background.

```html
<!DOCTYPE html>
<html lang="es">
<head>
<meta charset="utf-8">
<title>Vorelin — tarjetas de presentación</title>
<link rel="stylesheet" href="https://fonts.googleapis.com/css2?family=Open+Sans:wght@400;600&display=swap">
<style>
  :root {
    --backdrop: #e9e6e1;
    --front-bg: #ffffff;
    --brand-blue: #123f8c;
    --blue-muted: #4a6aa6;
    --rule: #9fb2d6;
    --back-light: #2f63bf;
    --back-dark: #0b2a66;
    --back-text: #ffffff;
  }
  * { box-sizing: border-box; margin: 0; padding: 0; }
  html, body { width: 1200px; height: 432px; overflow: hidden; }
  body {
    background: var(--backdrop);
    font-family: "Open Sans", Arial, sans-serif;
    position: relative;
  }
  .card { position: absolute; border-radius: 24px; overflow: hidden; box-shadow: 0 2px 10px rgba(0,0,0,0.18); }

  /* Front */
  .card-front {
    left: 60px; top: 72px; width: 560px; height: 288px;
    background: var(--front-bg); color: var(--brand-blue);
  }
  .brand-mark {
    position: absolute; display: flex; align-items: center; gap: 12px;
  }
  .brand-mark .dot { width: 14px; height: 14px; border-radius: 50%; background: var(--brand-blue); flex: none; }
  .brand-mark .name { font-weight: 400; color: var(--brand-blue); line-height: 1; }
  .card-front .brand-mark { left: 40px; top: 96px; }
  .card-front .brand-mark .name { font-size: 62px; }
  .holder { position: absolute; left: 296px; top: 32px; width: 230px; text-align: center; }
  .holder .person { font-size: 15px; white-space: nowrap; }
  .holder .role { font-size: 12px; color: var(--blue-muted); margin-top: 6px; }
  .divider { position: absolute; left: 0; right: 0; top: 172px; height: 1px; background: var(--rule); }
  .contact { position: absolute; font-size: 11.5px; color: var(--brand-blue); line-height: 1; }
  .contact-line { display: flex; align-items: center; gap: 8px; height: 20px; white-space: nowrap; }
  .contact-line svg { width: 10px; height: 10px; flex: none; fill: var(--brand-blue); }
  .contact-phones { left: 30px; top: 190px; }
  .contact-email { left: 30px; top: 252px; }
  .contact-address { left: 360px; top: 190px; }
  .contact-address p { height: 20px; display: flex; align-items: center; }
  .contact-web { left: 340px; top: 252px; }

  /* Back */
  .card-back {
    left: 648px; top: 76px; width: 470px; height: 284px;
    background: radial-gradient(ellipse at 50% 42%, var(--back-light) 0%, #1f4ea3 45%, var(--back-dark) 100%);
    color: var(--back-text);
  }
  .card-back .brand-mark { left: 0; right: 0; top: 112px; justify-content: center; gap: 10px; }
  .card-back .brand-mark .dot { background: var(--back-text); width: 10px; height: 10px; }
  .card-back .brand-mark .name { font-size: 40px; color: var(--back-text); }
  .back-firm { position: absolute; left: 0; right: 0; top: 166px; text-align: center; font-size: 12px; letter-spacing: 3px; text-transform: uppercase; }
  .back-web { position: absolute; left: 0; right: 0; top: 230px; text-align: center; font-size: 11px; letter-spacing: 2px; }
</style>
</head>
<body>
  <section class="card card-front" aria-label="Cara frontal">
    <div class="holder">
      <p class="person">Lucila Barrios Quintero</p>
      <p class="role">Presidente</p>
    </div>
    <div class="brand-mark"><span class="dot"></span><span class="name">Vorelin</span></div>
    <div class="divider"></div>
    <div class="contact contact-phones">
      <p class="contact-line"><svg viewBox="0 0 10 10"><path d="M2 0.5h2l0.8 2.4-1.3 0.9a6 6 0 0 0 2.7 2.7l0.9-1.3 2.4 0.8v2a1 1 0 0 1-1 1A8 8 0 0 1 1 1.5a1 1 0 0 1 1-1z"/></svg>571-4417290</p>
      <p class="contact-line"><svg viewBox="0 0 10 10"><rect x="2.5" y="0.5" width="5" height="9" rx="1"/></svg>57-3157702418 / 57-3208815296</p>
      <p class="contact-line"><svg viewBox="0 0 10 10"><path d="M1 2h8v6H1z M2.5 3.5v2h5v-2z" fill-rule="evenodd"/></svg>571-4417315</p>
    </div>
    <p class="contact contact-email contact-line"><svg viewBox="0 0 10 10"><path d="M0.5 2h9v6h-9z M1.2 2.6l3.8 3 3.8-3" fill-rule="evenodd"/></svg>lucilabarriosquintero@correoplum.net</p>
    <div class="contact contact-address">
      <p>Av. Carrera 57 #18B-64</p>
      <p>Bogota, Colombia</p>
    </div>
    <p class="contact contact-web contact-line"><svg viewBox="0 0 10 10"><circle cx="5" cy="5" r="4.5"/></svg>www.vorelin-demo.net</p>
  </section>

  <section class="card card-back" aria-label="Cara posterior">
    <div class="brand-mark"><span class="dot"></span><span class="name">Vorelin</span></div>
    <p class="back-firm">Montclaro SAS</p>
    <p class="back-web">www.vorelin-demo.net</p>
  </section>
</body>
</html>
```